Lucia Verena a furniture, interior design and home decor Brand

I need complete stationary for a new brand, business card, postcard, letter head, shipping envelopes, tissue paper, etc... I would like to use copper foil on some of these items. I have a logo design. I would like to see

Target Market(s)

Furniture,Interior Design & Home Decor

Industry/Entity Type

Interior Design

Colors
606060
7f7f7f

Requirements
Must have
• My signature style is spanish medeterrenean, my brand colors is charcoal gray with copper. Would love to see a wrought iron panel illustration created, I have attahced a few samples of wrought iron illustration I am attracted to, also an example of packing that has the pattern in foil.
Should not have
• Will not be using the word Design, only Lucia Verena and LV icon

```html
<!DOCTYPE html>
<html lang="en">
<head>
<meta charset="utf-8">
<title>Lucia Verena Letterhead</title>
<link href="https://fonts.googleapis.com/css2?family=Arimo:wght@400&display=swap" rel="stylesheet">
<style>
  :root {
    --backdrop: #dfb297;
    --paper: #fffdfb;
    --copper: #c9774c;
    --text-grey: #8d8d8d;
    --charcoal: #606060;
    --photo-dark: #5a4a3c;
    --photo-mid: #9a8470;
    --photo-light: #d9cbb8;
    --signature-tone: #ececec;
  }
  * { margin: 0; padding: 0; box-sizing: border-box; }
  html, body { width: 1200px; height: 784px; overflow: hidden; }
  body {
    background: var(--backdrop);
    font-family: "Arimo", Arial, sans-serif;
    position: relative;
  }
  .letterhead {
    position: absolute;
    left: 340px; top: 24px;
    width: 520px; height: 736px;
    background: var(--paper);
    box-shadow: 0 6px 18px rgba(120, 70, 40, 0.25);
    overflow: hidden;
  }
  .corner-art {
    position: absolute;
    left: 0; top: 0;
    width: 520px; height: 736px;
  }
  .brand-header {
    position: absolute;
    left: 30px; top: 26px;
    display: flex;
    align-items: center;
  }
  .brand-mark {
    width: 34px; height: 34px;
    border: 1.5px solid var(--copper);
    border-radius: 50%;
    margin-right: 8px;
  }
  .brand-name {
    color: var(--copper);
    font-size: 15px;
    letter-spacing: 0.3px;
  }
  .header-divider {
    width: 1px; height: 44px;
    background: var(--copper);
    margin: 0 10px 0 12px;
  }
  .contact-list { list-style: none; }
  .contact-list li {
    font-size: 6.5px;
    line-height: 9px;
    color: var(--text-grey);
    display: flex;
    align-items: center;
  }
  .contact-list li:first-child { color: var(--copper); }
  .contact-icon {
    width: 5px; height: 5px;
    border-radius: 50%;
    background: var(--copper);
    margin-right: 4px;
    flex: none;
  }
  .letter-body {
    position: absolute;
    left: 96px; top: 150px;
    width: 330px;
    color: var(--text-grey);
    font-size: 9px;
    line-height: 12.5px;
  }
  .letter-body p { margin-bottom: 14px; }
  .letter-body .lead-paragraph { margin-left: 28px; }
  .signature {
    position: absolute;
    left: 170px; top: 560px;
    width: 150px; height: 46px;
    background: var(--signature-tone);
    border-radius: 4px;
  }
</style>
</head>
<body>
  <article class="letterhead">
    <svg class="corner-art" viewBox="0 0 520 736">
      <defs>
        <linearGradient id="interior-tones" x1="0" y1="0" x2="1" y2="1">
          <stop offset="0" stop-color="#9a8470"/>
          <stop offset="0.5" stop-color="#5a4a3c"/>
          <stop offset="1" stop-color="#d9cbb8"/>
        </linearGradient>
      </defs>
      <g class="corner-panel corner-panel--top">
        <polygon points="300,0 520,0 520,100 420,110" fill="url(#interior-tones)" role="img" aria-label="Interior photograph of a furnished living room"/>
        <polyline points="290,0 415,118 520,110" fill="none" stroke="#ffffff" stroke-width="3"/>
        <polyline points="278,0 411,127 520,119" fill="none" stroke="#ffffff" stroke-width="2"/>
        <polyline points="266,0 407,136 520,128" fill="none" stroke="#ffffff" stroke-width="2"/>
      </g>
      <g class="corner-panel corner-panel--bottom">
        <polygon points="0,660 180,640 380,736 0,736" fill="url(#interior-tones)" role="img" aria-label="Interior photograph of a decorated room with furniture"/>
        <polyline points="0,650 186,630 400,736" fill="none" stroke="#ffffff" stroke-width="3"/>
        <polyline points="0,640 190,620 420,736" fill="none" stroke="#ffffff" stroke-width="2"/>
        <polyline points="0,630 194,610 440,736" fill="none" stroke="#ffffff" stroke-width="2"/>
      </g>
    </svg>

    <header class="brand-header">
      <span class="brand-mark"></span>
      <span class="brand-name">Lucia Verena</span>
      <span class="header-divider"></span>
      <ul class="contact-list">
        <li><span class="contact-icon"></span>Level 00, 00 Example Street, Example, 0000</li>
        <li><span class="contact-icon"></span>000 000 129 | 000 000 130</li>
        <li><span class="contact-icon"></span>contact@luciaverena.com</li>
        <li><span class="contact-icon"></span>www.luciaverena.com</li>
      </ul>
    </header>

    <section class="letter-body">
      <p class="lead-paragraph">Lorem Ipsum is simply dummy text of the printing and typesetting industry. Lorem Ipsum has been the industry's standard dummy text ever since the 1500s, when an unknown printer took a galley of type and scrambled it to make a type specimen book. It has survived not only five centuries, but also the leap into electronic typesetting, remaining essentially unchanged. It was popularised in the 1960s with the release of Typeleaf sheets containing Lorem Ipsum passages, and more recently with desktop publishing software like Pagewright Studio including versions of Lorem Ipsum.</p>
      <p>It is a long established fact that a reader will be distracted by the readable content of a page when looking at its layout. The point of using Lorem Ipsum is that it has a more-or-less normal distribution of letters, as opposed to using 'Content here, content here', making it look like readable English. Many desktop publishing packages and web page editors now use Lorem Ipsum as their default model text, and a search for 'lorem ipsum' will uncover many web sites still in their infancy. Various versions have evolved over the years, sometimes by accident, sometimes on purpose (injected humour and the like).</p>
      <p>Contrary to popular belief, Lorem Ipsum is not simply random text. It has roots in a piece of classical Latin literature from 45 BC, making it over 2000 years old. Marco Bellan, a Latin professor at Ashford Hill College in Example Valley, looked up one of the more obscure Latin words, consectetur, from a Lorem Ipsum passage, and going through the cites of the word in classical literature, discovered the undoubtable source. Lorem Ipsum comes from sections 1.10.32 and 1.10.33 of "de Finibus Bonorum et Malorum" structures, to generate Lorem Ipsum which looks reasonable. The generated Lorem Ipsum is therefore always free from repetition, injected humour, or non-characteristic words etc.</p>
    </section>

    <div class="signature" role="img" aria-label="Handwritten signature of the sender"></div>
  </article>
</body>
</html>
```